Business card design for Plumbing and Gas fitting company

We need a business card design for our plumbing and gas fitting company using the company logo and director details. Design should be modern and eye-catching however kept reasonably simple. This design should be targeted at commercial businesses/work so professionalism is key.

Target Market(s)

Commercial/business

Industry/Entity Type

Plumbing

Contact Information for Business Card

Warren Dohey
Director
027 581 9043
warren@vantorplumbingandgas.example
PO Box 7816
Palmerston North 4472

Font styles to use
Sans Serif

Requirements
Must have
• Logo
• Modern
• Kept simple
Nice to have
• Colour scheme based around logo

```html
<!DOCTYPE html>
<html lang="en">
<head>
<meta charset="utf-8">
<title>Vantor Plumbing &amp; Gas – Business Card</title>
<link href="https://fonts.googleapis.com/css2?family=Quicksand:wght@500;700&display=swap" rel="stylesheet">
<style>
  :root {
    --brand-blue: #1170bf;
    --brand-grey: #7a7a7a;
    --brand-orange: #ec7a2f;
    --panel-dark: #2c2c2e;
    --card-white: #ffffff;
    --backdrop: #e7e4df;
    --text-light: #f2f2f2;
    --text-muted: #9a9a9a;
  }
  * { margin: 0; padding: 0; box-sizing: border-box; }
  html, body { width: 1200px; height: 788px; overflow: hidden; }
  body {
    background: var(--backdrop);
    font-family: "Quicksand", sans-serif;
    position: relative;
  }
  .card {
    position: absolute;
    top: 260px;
    width: 480px;
    height: 267px;
    background: var(--card-white);
    overflow: hidden;
    box-shadow: 0 2px 6px rgba(0,0,0,.18);
  }
  .card--front { left: 110px; }
  .card--back { left: 635px; }

  /* Front */
  .front-brand {
    position: absolute;
    left: 0; right: 0; top: 92px;
    display: flex; align-items: center; justify-content: center; gap: 14px;
  }
  .brand-dot {
    width: 46px; height: 46px; border-radius: 50%;
    background: var(--brand-blue);
    flex: none;
  }
  .brand-name {
    color: var(--brand-blue);
    font-weight: 700;
    line-height: 1.05;
  }
  .front-brand .brand-name { font-size: 30px; }
  .front-band { position: absolute; left: 0; bottom: 0; width: 480px; height: 36px; }

  /* Back */
  .back-brand {
    position: absolute; left: 16px; top: 20px;
    display: flex; align-items: center; gap: 10px;
  }
  .back-brand .brand-dot { width: 30px; height: 30px; }
  .back-brand .brand-name { font-size: 18px; }
  .back-panel { position: absolute; left: 216px; top: 0; width: 264px; height: 267px; }
  .contact-icon {
    position: absolute; left: 8px;
    width: 28px; height: 28px; border-radius: 50%;
    background: var(--card-white);
    display: flex; align-items: center; justify-content: center;
  }
  .contact-icon svg { width: 13px; height: 13px; fill: var(--panel-dark); }
  .person-name {
    position: absolute; left: 65px; top: 23px;
    color: var(--text-light); font-weight: 700; font-size: 19px;
  }
  .person-role {
    position: absolute; left: 65px; top: 48px;
    color: var(--text-muted); font-weight: 500; font-size: 11px; letter-spacing: .5px;
  }
  .contact-text {
    position: absolute; left: 53px;
    color: var(--text-light); font-weight: 500; font-size: 11px; line-height: 1.3;
    white-space: nowrap;
  }
  .contact-text--email { font-size: 9.5px; }
</style>
</head>
<body>

<section class="card card--front">
  <div class="front-brand">
    <span class="brand-dot"></span>
    <span class="brand-name">Vantor Plumbing &amp; Gas</span>
  </div>
  <svg class="front-band" viewBox="0 0 480 36" aria-hidden="true">
    <path d="M0 13 H236 C246 13 248 3 252 3 C256 3 258 13 268 13 H480 V36 H0 Z" fill="var(--brand-blue)" transform="translate(-12 0)"/>
    <rect x="468" y="13" width="12" height="23" fill="var(--brand-blue)"/>
  </svg>
</section>

<section class="card card--back">
  <div class="back-brand">
    <span class="brand-dot"></span>
    <span class="brand-name">Vantor Plumbing<br>&amp; Gas</span>
  </div>

  <div class="back-panel">
    <svg width="264" height="267" viewBox="0 0 264 267" aria-hidden="true" style="position:absolute;left:0;top:0">
      <rect x="0" y="0" width="34" height="267" fill="var(--brand-blue)"/>
      <rect x="34" y="0" width="230" height="267" fill="var(--panel-dark)"/>
      <path d="M34 36 L46 46 L34 56 Z" fill="var(--brand-blue)"/>
      <path d="M34 126 L46 136 L34 146 Z" fill="var(--brand-blue)"/>
      <path d="M34 174 L46 184 L34 194 Z" fill="var(--brand-blue)"/>
      <path d="M34 222 L46 232 L34 242 Z" fill="var(--brand-blue)"/>
    </svg>

    <span class="contact-icon" style="top:32px">
      <svg viewBox="0 0 24 24"><circle cx="12" cy="8" r="5"/><path d="M2 23c0-6 4-9 10-9s10 3 10 9z"/></svg>
    </span>
    <p class="person-name">Warren Dohey</p>
    <p class="person-role">DIRECTOR</p>

    <span class="contact-icon" style="top:122px">
      <svg viewBox="0 0 24 24"><path d="M6.6 10.8a15 15 0 0 0 6.6 6.6l2.2-2.2c.3-.3.7-.4 1-.2 1.1.4 2.3.6 3.6.6.6 0 1 .4 1 1V20c0 .6-.4 1-1 1A17 17 0 0 1 3 4c0-.6.4-1 1-1h3.5c.6 0 1 .4 1 1 0 1.3.2 2.5.6 3.6.1.3 0 .7-.2 1z"/></svg>
    </span>
    <p class="contact-text" style="top:129px">027 581 9043</p>

    <span class="contact-icon" style="top:170px">
      <svg viewBox="0 0 24 24"><path d="M12 2a10 10 0 1 0 0 20 10 10 0 0 0 0-20zm7.9 9h-3.4a15 15 0 0 0-1.3-6.1A8 8 0 0 1 19.9 11zM12 4c1 1.3 2.3 3.8 2.5 7h-5C9.7 7.8 11 5.3 12 4zM8.8 4.9A15 15 0 0 0 7.5 11H4.1a8 8 0 0 1 4.7-6.1zM4.1 13h3.4a15 15 0 0 0 1.3 6.1A8 8 0 0 1 4.1 13zM12 20c-1-1.3-2.3-3.8-2.5-7h5c-.2 3.2-1.5 5.7-2.5 7zm3.2-.9a15 15 0 0 0 1.3-6.1h3.4a8 8 0 0 1-4.7 6.1z"/></svg>
    </span>
    <p class="contact-text contact-text--email" style="top:178px">warren@vantorplumbingandgas.example</p>

    <span class="contact-icon" style="top:218px">
      <svg viewBox="0 0 24 24"><path d="M12 1a8 8 0 0 0-8 8c0 6 8 14 8 14s8-8 8-14a8 8 0 0 0-8-8zm0 11a3 3 0 1 1 0-6 3 3 0 0 1 0 6z"/></svg>
    </span>
    <p class="contact-text" style="top:218px">PO Box 7816<br>Palmerston North 4472</p>
  </div>
</section>

</body>
</html>
```